Brackenfield Partners Exit Plan business consultant web site

This website is for a consulting business that helps other businesses with exit plans. Essentially, assists them with the sale of their business. This website should be very professional, almost with a wall street look. I would like a very attractive image on the homepage. Perhaps something that denotes success. Perhaps a picture of palm trees and a beach? I will leave it to you for interpretation.

Across the screen I would like the words "Does your business have an exit plan?"

Below that it should read the following:
Let us help you with a completely impartial, no obligation assessment (button with link to the contact page)

Also, please use logo in a prominent place on the website so it's easily seen.

Target Market(s)

Males 40+

Coding

Coded - Design and coding required

Number of Pages Required

5+ page

Colors

Designer to choose colors to be used in the design.

Requirements
Must have
• The tabs for the homepage on the top should be:
• 1. About us
• 2. Services
• 3. Industries
• 4. Our success
• 5. Contact
Nice to have
• Clean, professional image.
• Please put FB, Twitter, Linked In - logos at bottom.
• Here are two examples of a website to give you an idea:
• https://journal.corvanteriq.com/library/why-every-business-owner-should-have-an-exit-plan
Should not have
• nothing whimsical or cartoon like

```html
<!DOCTYPE html>
<html lang="en">
<head>
<meta charset="utf-8">
<title>Brackenfield Partners – Exit Plan Consultants</title>
<link href="https://fonts.googleapis.com/css2?family=Poppins:wght@400;500;600;700;800&family=Lora:ital@1&display=swap" rel="stylesheet">
<style>
:root{
  --stage:#84fd8b;
  --navy:#22274a;
  --navy-line:#363c63;
  --green:#8dc63f;
  --ink:#1e2240;
  --muted:#6b6f80;
  --white:#ffffff;
  --mist:#eef2f7;
}
*{margin:0;padding:0;box-sizing:border-box}
html,body{width:1200px;height:2400px;overflow:hidden;background:var(--stage);font-family:"Poppins",sans-serif;color:var(--ink)}
.stage{position:absolute;left:0;top:0;width:1288px;height:2576px;transform:scale(0.93168);transform-origin:0 0}
.page{position:absolute;left:267px;top:108px;width:754px;height:2358px;background:var(--white);box-shadow:0 10px 40px rgba(0,60,0,.35);overflow:hidden}
.abs{position:absolute}
.photo{position:absolute}
/* header */
.brand{left:48px;top:30px;font-size:11px;font-weight:500;letter-spacing:.5px;color:var(--ink);display:flex;align-items:center;gap:6px;white-space:nowrap}
.brand i{width:10px;height:10px;background:var(--ink);display:block}
.nav{left:298px;top:43px;font-size:10px}
.nav a{position:absolute;white-space:nowrap;color:var(--ink);text-decoration:none}
.nav a.on{color:var(--green)}
.caret{font-size:7px}
/* hero */
.hero{left:0;top:69px;width:754px;height:369px;background:linear-gradient(135deg,#6e6a66,#403b38 45%,#5b5552 75%,#8c8782)}
.hero-title{left:0;top:172px;width:754px;text-align:center;color:#fff;font-weight:800;font-size:43px;line-height:52px;letter-spacing:.5px;text-transform:uppercase}
.hero-sub{left:0;top:280px;width:754px;text-align:center;color:#fff;font-size:13px;font-weight:500}
.btn{background:var(--green);color:#fff;font-weight:600;display:flex;align-items:center;justify-content:center;white-space:nowrap}
.hero-btn{left:325px;top:311px;width:104px;height:31px;font-size:13px}
/* about */
.eyebrow{font-size:8px;color:var(--green);font-weight:500}
.h-about{left:142px;top:494px;font-size:17px;font-weight:700;line-height:20px}
.small{font-size:5.5px;line-height:11px;color:var(--muted)}
.item-title{font-size:8.5px;font-weight:500}
.learn{left:160px;top:714px;width:92px;height:24px;font-size:8.5px}
.about-photo{left:420px;top:488px;width:334px;height:202px;background:linear-gradient(120deg,#c9ccd0,#7c8087 50%,#3b3f48)}
.play{left:664px;top:488px;width:90px;height:30px;background:var(--green);color:#fff;font-size:5px;font-weight:600;display:flex;align-items:center;justify-content:center;gap:5px}
.play i{width:9px;height:9px;border:1px solid #fff;border-radius:50%;display:block}
.years{left:383px;top:644px;width:103px;height:69px;background:#fff;border:2px dashed #c7c7c7;text-align:center;color:var(--green)}
.years b{display:block;font-size:22px;margin-top:10px;font-weight:600}
.years span{font-size:7px}
/* services */
.band{left:0;width:754px;background:var(--navy)}
.h-light{color:#fff;font-size:20px;font-weight:500;white-space:nowrap}
.arrow{width:23px;height:23px;border-radius:50%;display:flex;align-items:center;justify-content:center;color:#fff;font-size:10px}
.card{top:897px;width:142px;height:174px;border:1px solid var(--navy-line);text-align:center;color:#fff}
.card.active{border:1px solid var(--green)}
.card svg{margin-top:22px}
.card h3{font-size:8.5px;font-weight:500;margin-top:10px}
.card p{font-size:5.5px;line-height:11px;color:#c9cbe0;margin:10px 10px 0}
.card .go{width:14px;height:14px;border-radius:50%;margin:10px auto 0;background:var(--navy-line);color:var(--green);font-size:7px;display:flex;align-items:center;justify-content:center}
.card.active .go{width:16px;height:16px;background:var(--green);color:#fff}
/* team */
.center{left:0;width:754px;text-align:center}
.h-dark{font-size:20px;font-weight:500;color:var(--ink)}
.member{top:1213px;width:142px;height:178px}
.social-bar{left:306px;top:1360px;width:142px;height:31px;background:var(--green);display:flex;justify-content:center;align-items:center;gap:9px}
.social-bar i{width:12px;height:12px;border-radius:50%;border:1px solid #fff;display:block}
.social-bar i:first-child{background:#fff}
.name{top:1405px;width:142px;text-align:center;font-size:9px;font-weight:500}
.role{top:1421px;width:142px;text-align:center;font-size:5.5px;color:var(--muted)}
/* testimonial */
.testi{left:0;top:1471px;width:754px;height:218px;background:var(--mist)}
.quote-text{left:152px;top:1522px;width:225px;font-family:"Lora",serif;font-style:italic;font-size:9px;line-height:15px;color:var(--ink)}
/* contact */
.field{left:421px;width:181px;border:1px solid var(--navy-line);color:#fff;font-size:5.5px;padding:8px 10px}
.info{left:38px;top:1770px;width:130px;height:58px;background:#2f3560;color:#fff;padding:6px 11px;font-size:6px;line-height:11px;white-space:nowrap}
.info small{font-size:5px;display:block;line-height:12px}
/* footer */
.foot-brand{left:95px;top:2248px;width:230px;text-align:center;color:#fff;font-size:16px;font-weight:500;letter-spacing:.5px;display:flex;align-items:center;justify-content:center;gap:8px;white-space:nowrap}
.foot-brand i{width:14px;height:14px;background:#fff;display:block}
.foot-h{font-size:9px;font-weight:500;color:#fff}
.foot-list{font-size:5.5px;line-height:14px;color:#d7d9ea;list-style:none;white-space:nowrap}
.dot{width:14px;height:14px;border-radius:50%;display:block;background:var(--navy-line)}
</style>
</head>
<body>
<div class="stage">
<div class="page">

  <header>
    <div class="abs brand"><i></i>Brackenfield Partners</div>
    <nav class="abs nav">
      <a class="on" style="left:0">Home</a>
      <a style="left:57px">About us</a>
      <a style="left:128px">Services<span class="caret"> ▾</span></a>
      <a style="left:199px">Industries<span class="caret"> ▾</span></a>
      <a style="left:270px">Our success</a>
      <a style="left:355px">Contact</a>
    </nav>
  </header>

  <section class="hero-section">
    <div class="photo hero" role="img" aria-label="Business partners shaking hands across a meeting table"></div>
    <h1 class="abs hero-title">Does your business<br>have an exit plan?</h1>
    <p class="abs hero-sub">Let us help you with a completely impartial, no obligation assessment</p>
    <a class="abs btn hero-btn">Contact Us</a>
  </section>

  <section class="about">
    <div class="abs eyebrow" style="left:142px;top:476px">About Us</div>
    <h2 class="abs h-about">A World Class Exit Plan<br>Business Consultant</h2>
    <p class="abs small" style="left:152px;top:546px;width:220px">We guide owners through every stage of leaving their company, from valuation and buyer search to a smooth and rewarding sale of the business they built.</p>
    <svg class="abs" style="left:152px;top:590px" width="22" height="22" viewBox="0 0 22 22" fill="none" stroke="#8dc63f" stroke-width="1"><circle cx="11" cy="9" r="6"/><path d="M8 15h6M9 18h4"/></svg>
    <div class="abs item-title" style="left:183px;top:590px">Business Exit Plan</div>
    <p class="abs small" style="left:187px;top:604px;width:115px">A clear roadmap that shows you when and how to step away with the best value.</p>
    <svg class="abs" style="left:150px;top:645px" width="24" height="20" viewBox="0 0 24 20" fill="none" stroke="#8dc63f" stroke-width="1"><rect x="1" y="4" width="17" height="11"/><circle cx="9.5" cy="9.5" r="3"/><path d="M20 8v10M22 8v10"/></svg>
    <div class="abs item-title" style="left:187px;top:646px;font-size:7px">Finance Solution</div>
    <p class="abs small" style="left:187px;top:658px;width:115px">Funding and tax advice that keeps more of the sale proceeds in your pocket.</p>
    <a class="abs btn learn">Learn More</a>
    <div class="photo about-photo" role="img" aria-label="Two consultants reviewing work on a laptop in an office"></div>
    <div class="abs play"><i></i>PLAY VIDEO</div>
    <div class="abs years"><b>28</b><span>Years Of Experience</span></div>
  </section>

  <section class="abs band" style="top:788px;height:326px"></section>
  <div class="abs eyebrow" style="left:150px;top:832px">Our Services</div>
  <h2 class="abs h-light" style="left:150px;top:851px">See Our Best Services</h2>
  <div class="abs arrow" style="left:543px;top:844px;background:var(--navy-line)">‹</div>
  <div class="abs arrow" style="left:579px;top:844px;background:var(--green)">›</div>

  <div class="abs card" style="left:152px">
    <svg width="30" height="34" viewBox="0 0 30 34" fill="none" stroke="#8dc63f" stroke-width="1.2"><circle cx="14" cy="13" r="9"/><path d="M10 24h8M11 28h6M24 3l2-2"/></svg>
    <h3>Exit Plan Strategy</h3>
    <p>A tailored plan that sets timing, value targets and succession for a confident exit.</p>
    <div class="go">→</div>
  </div>
  <div class="abs card active" style="left:306px">
    <svg width="34" height="30" viewBox="0 0 34 30" fill="none" stroke="#8dc63f" stroke-width="1.2"><rect x="2" y="6" width="22" height="14"/><circle cx="13" cy="13" r="4"/><ellipse cx="28" cy="17" rx="4" ry="2"/><path d="M24 17v9c0 1 8 1 8 0v-9"/></svg>
    <h3>Finance Solution</h3>
    <p>Financial structuring and tax planning to protect the proceeds of your sale.</p>
    <div class="go">→</div>
  </div>
  <div class="abs card" style="left:460px">
    <svg width="30" height="32" viewBox="0 0 30 32" fill="none" stroke="#8dc63f" stroke-width="1.2"><path d="M4 2h18l5 5v23H4z"/><circle cx="12" cy="14" r="5"/><path d="M8 26l6-5 4 3 6-6"/></svg>
    <h3>Business Planing</h3>
    <p>Growth plans that raise value and make your company more attractive to buyers.</p>
    <div class="go">→</div>
  </div>

  <section class="team">
    <div class="abs center eyebrow" style="top:1154px">Our Team</div>
    <h2 class="abs center h-dark" style="top:1168px">Discover Trust Team</h2>
    <div class="photo member" style="left:152px;background:linear-gradient(160deg,#c7c9cc,#5b5f66)" role="img" aria-label="Portrait of the chief executive in a dark suit"></div>
    <div class="photo member" style="left:306px;background:linear-gradient(160deg,#8e94a8,#4a4f66)" role="img" aria-label="Portrait of the interface designer"></div>
    <div class="photo member" style="left:460px;background:linear-gradient(160deg,#e6e8e3,#8aa6c9)" role="img" aria-label="Portrait of the web developer in a blue shirt"></div>
    <div class="abs social-bar"><i></i><i></i><i></i><i></i></div>
    <div class="abs name" style="left:152px">Daniel Ashworth</div>
    <div class="abs role" style="left:152px">CEO &amp; Founder</div>
    <div class="abs name" style="left:306px">Clara Whitcombe</div>
    <div class="abs role" style="left:306px">UI Designer</div>
    <div class="abs name" style="left:460px">Oliver Pennick</div>
    <div class="abs role" style="left:460px">Web Developer</div>
  </section>

  <section class="abs testi"></section>
  <div class="photo" style="left:430px;top:1478px;width:165px;height:211px;background:linear-gradient(180deg,#eef2f7,#b7d6d4 50%,#1aa39a)" role="img" aria-label="Smiling woman in a teal top presenting with an open hand"></div>
  <svg class="abs" style="left:114px;top:1496px" width="66" height="52" viewBox="0 0 66 52" fill="none" stroke="#c8dca8" stroke-width="3"><path d="M28 6C14 6 4 18 4 32s6 16 12 16 10-6 10-12-4-10-10-10M62 6C48 6 38 18 38 32s6 16 12 16 10-6 10-12-4-10-10-10"/></svg>
  <p class="abs quote-text">They listened first, then built an exit plan that fit our family and our staff. The sale closed on time and above the value we had hoped for, and every step of the process was clear.</p>
  <div class="abs" style="left:152px;top:1620px;font-size:6px;font-weight:500">Helena Marlow</div>
  <div class="abs" style="left:152px;top:1630px;font-size:5px;color:var(--green)">- UI Designer</div>

  <section class="abs band" style="top:1689px;height:350px"></section>
  <div class="photo" style="left:38px;top:1770px;width:358px;height:190px;background:radial-gradient(ellipse at 55% 45%,#3d4475,#2a3058 70%,#22274a)" role="img" aria-label="World map with office locations marked"></div>
  <div class="abs info">United State<br>Head Office<small>☎ +1 555 0142 880</small><small>✉ hello@brackenfield.example</small></div>
  <div class="abs eyebrow" style="left:417px;top:1741px">Contact Us</div>
  <h2 class="abs h-light" style="left:421px;top:1751px">Request A Call Back</h2>
  <div class="abs field" style="top:1800px;height:25px">Name</div>
  <div class="abs field" style="top:1838px;height:25px">Email</div>
  <div class="abs field" style="top:1876px;height:74px">Your Message</div>
  <a class="abs btn" style="left:421px;top:1962px;width:77px;height:25px;font-size:5px">SUBMIT NOW ›</a>

  <footer>
    <div class="abs band" style="top:2155px;height:203px"></div>
    <div class="abs foot-brand"><i></i>Brackenfield Partners</div>
    <div class="abs foot-h" style="left:348px;top:2205px">Usefull Links</div>
    <ul class="abs foot-list" style="left:348px;top:2222px"><li>About Company</li><li>Meet Experts</li><li>Our Case Studies</li><li>Get a Quote</li><li>Testimonials</li></ul>
    <ul class="abs foot-list" style="left:425px;top:2222px"><li>Our Services</li><li>Latest News</li><li>Privacy Policy</li></ul>
    <div class="abs foot-h" style="left:502px;top:2205px">Contact Us</div>
    <ul class="abs foot-list" style="left:502px;top:2222px"><li>212 Larchmont Avenue, Suite 9, NY 10014</li><li>United States</li><li>office@brackenfield.example</li><li>Mon - Fri: 9am to 6pm, W.E/ Holiday</li></ul>
    <div class="abs" style="left:502px;top:2292px;display:flex;gap:9px"><i class="dot" style="background:var(--green)"></i><i class="dot"></i><i class="dot"></i></div>
  </footer>

</div>
</div>
</body>
</html>
```